New Wordpress Design Project: KV- Kindred Vantage, Training Beyond Equity, Diversity, and Inclusion

I need a clean, modern, website design for KV- a national consulting firm providing equity, diversity, and inclusion training, through the lens of undoing racism, for arts and culture, and the non profit industry. It will feature both written posts, and some video. People will need KV contact information, and subscribe to receive information. It will feature a pretty active blog, and a section for resources, with links to other sites. There needs to be a section about KV,its training, approach, and bio Information. I probably should have put this first!

I want a site that draws people in. That is interesting and dynamic. My approach to this work is to provide people with the information, knowledge, and tools they need to go back to their communities and do the work. So they are at the center of the story. And I like powerful imagery. It could also be pretty.

The idea of undoing racism is a big idea. It is powerful, heroic even. And thousands of people in the US are working hard to do just that. So there is a sense of movement building here, of connecting to something important.

I already have a logo design that was done through a contest here last month.

Target Market(s)

Arts and culture fields, non profit industry, and philanthropy

Font styles to use
Sans Serif

Requirements
Must have
• Must have dynamic powerful imagery, be clean and easy to navigate, support concept of story telling, good use of color, be inviting, draw people in to learn when they see it first time. The ability to update photos, and videos easily. Connect to social media, especially Facebook and LinkedIn.
Nice to have
• It would be nice to have a website that uses more images than words to tell stories. I don't know enough about what's possible in website design to add more to this section.
Should not have
• Should not look like we are selling products, or services even but, rather, providing essential information and knowledge to help people make this world a better place for more people.

```html
<!DOCTYPE html>
<html lang="en">
<head>
<meta charset="utf-8">
<title>Kindred Vantage</title>
<link href="https://fonts.googleapis.com/css2?family=Open+Sans:wght@300;400;600;700&display=swap" rel="stylesheet">
<style>
:root{
  --yellow:#f7d800;
  --yellow-deep:#e9c800;
  --ink:#1f1f1f;
  --text:#555;
  --muted:#888;
  --rule:#dcdcdc;
  --panel:#f2f2f2;
  --white:#fff;
  --sky-top:#5b6d86;
  --sky-bottom:#9fb0c4;
}
*{box-sizing:border-box;margin:0;padding:0}
html,body{width:1200px;height:2557px;overflow:hidden}
body{position:relative;background:var(--white);font-family:"Open Sans",Arial,sans-serif;color:var(--text)}
.abs{position:absolute}

/* hero */
.hero{left:0;top:0;width:1200px;height:532px;background:linear-gradient(180deg,#3c4a5e 0%,var(--sky-top) 35%,var(--sky-bottom) 60%,#4a5a70 100%)}
.hero-shade{left:0;top:0;width:1200px;height:532px;background:linear-gradient(90deg,rgba(20,30,45,.55),rgba(20,30,45,.1) 40%,rgba(20,30,45,.1) 60%,rgba(20,30,45,.55))}
.brand{left:99px;top:8px;width:160px;height:96px;display:flex;flex-direction:column;align-items:center;gap:6px}
.brand-dot{width:50px;height:50px;border-radius:50%;background:var(--yellow)}
.brand-name{color:var(--white);font-size:19px;font-weight:400}
.topbar{right:75px;top:22px;display:flex;gap:36px;color:var(--white);font-size:16px}
.topbar span{display:flex;align-items:center;gap:10px}
.badge-icon{width:28px;height:28px;border-radius:50%;background:var(--yellow);display:flex;align-items:center;justify-content:center}
.nav{right:58px;top:74px;display:flex;gap:20px;font-size:16px;color:var(--white);align-items:center}
.nav .active{color:var(--yellow)}
.nav-rule{left:0;top:114px;width:1200px;height:1px;background:rgba(247,216,0,.5)}
.hero-title{left:0;top:162px;width:1200px;text-align:center;color:var(--white);font-size:74px;font-weight:300}
.hero-copy{left:250px;top:256px;width:700px;text-align:center;color:var(--white);font-size:17px;line-height:29px}
.cta{left:513px;top:336px;width:174px;height:41px;background:var(--yellow);color:var(--ink);font-weight:700;font-size:15px;display:flex;align-items:center;justify-content:center;border-radius:2px}
.arrow{top:248px}

.pillar{background:var(--white);border:4px solid var(--yellow);border-radius:50%;display:flex;flex-direction:column;align-items:center;justify-content:center;gap:14px;color:var(--ink);font-size:22px}

/* welcome */
.h2{color:var(--ink);font-weight:600}
.welcome-title{left:99px;top:718px;font-size:30px}
.body-copy{font-size:12.5px;line-height:22px;color:var(--text)}
.read-more{left:99px;top:975px;width:129px;height:32px;border:1px solid #999;color:var(--yellow-deep);font-size:11px;font-weight:700;display:flex;align-items:center;justify-content:center}
.media{left:605px;top:724px;width:496px;height:288px;border:1px solid var(--rule);padding:5px;background:var(--white)}
.media-fill{width:100%;height:100%;background:linear-gradient(135deg,#e9eef1,#c9d2d8 50%,#f1f3f4)}
.play{left:825px;top:837px;width:60px;height:60px;border-radius:50%;background:rgba(30,30,30,.8)}

/* services */
.services{left:0;top:1072px;width:1200px;height:402px;background:var(--yellow)}
.section-title{width:1200px;left:0;text-align:center;font-size:29px;color:var(--ink);font-weight:500}
.svc-title{font-size:18px;color:var(--ink);font-weight:600}
.svc-copy{font-size:12px;line-height:21px;color:#333;width:220px;margin-top:10px}

/* posts */
.card-img{border:1px solid var(--rule);padding:4px;background:var(--white)}
.card-fill{width:100%;height:100%}
.date{width:40px;height:54px;background:var(--yellow);color:var(--ink);text-align:center;font-size:24px;font-weight:700;line-height:30px}
.date small{display:block;font-size:12px;font-weight:400;line-height:16px}
.post-title{font-size:19px;font-weight:600;color:var(--ink)}
.post-copy{font-size:12px;line-height:21px;width:315px;color:var(--text)}
.post-rule{width:315px;height:1px;background:var(--rule)}
.meta{font-size:12px;color:var(--muted);display:flex;gap:18px}

/* blog */
.blog{left:0;top:2008px;width:1200px;height:222px;background:var(--panel)}
.blog-thumb{width:85px;height:75px;border:3px solid var(--white)}
.blog-title{font-size:17px;font-weight:600;color:#333}
.blog-date{font-size:12px;color:var(--muted);margin-top:10px}
.accent-rule{left:0;top:2230px;width:1200px;height:4px;background:var(--yellow)}

/* footer */
.foot-title{font-size:18px;color:var(--ink);font-weight:600}
.foot-list{list-style:none;font-size:12px;line-height:21px;color:#555;margin-top:14px}
.input{left:518px;top:2364px;width:254px;height:34px;border:1px solid #ccc;font-size:12px;color:#999;padding:9px 14px}
.subscribe{left:518px;top:2415px;width:92px;height:31px;border:1px solid #ccc;color:var(--yellow-deep);font-size:11px;font-weight:600;display:flex;align-items:center;justify-content:center}
.contact-row{display:flex;gap:16px;font-size:12px;line-height:20px;color:#555}
.bottom-rule{left:99px;top:2485px;width:1002px;height:1px;background:var(--rule)}
.copyright{left:99px;top:2512px;font-size:12px;color:#555}
.social{width:25px;height:25px;border:1px solid #aaa;border-radius:50%}
</style>
</head>
<body>

<header>
  <div class="abs hero" role="img" aria-label="Looking up between tall glass office towers against the sky"></div>
  <div class="abs hero-shade"></div>
  <div class="abs brand"><div class="brand-dot"></div><div class="brand-name">Kindred Vantage</div></div>
  <div class="abs topbar">
    <span><span class="badge-icon"><svg width="14" height="14" viewBox="0 0 24 24"><path fill="#222" d="M6.6 10.8a15 15 0 0 0 6.6 6.6l2.2-2.2c.3-.3.7-.4 1-.2 1.1.4 2.3.6 3.6.6.6 0 1 .4 1 1V20c0 .6-.4 1-1 1A17 17 0 0 1 3 4c0-.6.4-1 1-1h3.5c.6 0 1 .4 1 1 0 1.3.2 2.5.6 3.6.1.3 0 .7-.2 1z"/></svg></span>555-210-4471</span>
    <span><span class="badge-icon"><svg width="14" height="12" viewBox="0 0 24 18"><rect x="1" y="1" width="22" height="16" fill="#222"/><path d="M1 1l11 9 11-9" stroke="#f7d800" stroke-width="2" fill="none"/></svg></span>hello@kindredvantage.org</span>
  </div>
  <nav class="abs nav">
    <span class="active">Home</span><span>About us</span><span>Services</span><span>Blog</span><span>Insights &amp; News</span><span>Resources</span><span>Contact Us</span>
    <svg width="16" height="16" viewBox="0 0 24 24"><circle cx="10" cy="10" r="7" stroke="#fff" stroke-width="3" fill="none"/><path d="M15 15l7 7" stroke="#fff" stroke-width="3"/></svg>
  </nav>
  <div class="abs nav-rule"></div>
</header>

<section>
  <h1 class="abs hero-title">Kindred Vantage</h1>
  <p class="abs hero-copy">We are a national consulting firm providing equity, diversity, and inclusion training, through the lens of undoing racism, for arts and culture, and the non profit industry.</p>
  <div class="abs cta">GET A QUOTE</div>
  <svg class="abs arrow" style="left:40px" width="20" height="32" viewBox="0 0 20 32"><path d="M16 2L4 16l12 14" stroke="#fff" stroke-width="3" fill="none"/></svg>
  <svg class="abs arrow" style="right:40px" width="20" height="32" viewBox="0 0 20 32"><path d="M4 2l12 14L4 30" stroke="#fff" stroke-width="3" fill="none"/></svg>

  <div class="abs pillar" style="left:282px;top:443px;width:204px;height:204px">
    <svg width="86" height="74" viewBox="0 0 86 74"><rect x="30" y="4" width="50" height="36" stroke="#222" stroke-width="4" fill="none"/><path d="M38 32l10-10 8 6 14-14" stroke="#222" stroke-width="4" fill="none"/><path d="M55 40v12M55 52l-12 18M55 52l12 18" stroke="#222" stroke-width="4"/><rect x="6" y="26" width="18" height="44" fill="#222"/><circle cx="15" cy="16" r="8" fill="#222"/></svg>
    <span>Training</span>
  </div>
  <div class="abs pillar" style="left:476px;top:420px;width:244px;height:244px">
    <svg width="90" height="92" viewBox="0 0 90 92"><path d="M8 44L45 6l37 38M18 36v52h54V36" stroke="#222" stroke-width="4" fill="none"/><text x="45" y="72" text-anchor="middle" font-family="Open Sans,Arial,sans-serif" font-size="34" fill="#222">%</text><rect x="18" y="84" width="54" height="4" fill="#222"/></svg>
    <span>Equity</span>
  </div>
  <div class="abs pillar" style="left:713px;top:445px;width:200px;height:200px">
    <svg width="74" height="74" viewBox="0 0 74 74"><path d="M64 40A28 28 0 1 1 52 14" stroke="#222" stroke-width="8" fill="none"/><path d="M46 4l14 10-14 8z" fill="#222"/><path d="M36 22v16l10 8" stroke="#222" stroke-width="5" fill="none"/></svg>
    <span>Diversity</span>
  </div>
</section>

<section>
  <h2 class="abs h2 welcome-title">Welcome to Kindred Vantage</h2>
  <p class="abs body-copy" style="left:99px;top:775px;width:460px">At vero eos et accusamus et iusto odio dignissimos ducimus qui blanditiis prasent ium voluptatum deleniti atque corrupti quo.</p>
  <p class="abs body-copy" style="left:99px;top:851px;width:460px">Dolores et quas molestias excepturi sint occaecati cupiditate non provident similiq ue sunt in culpa qui officia deserunt mollitia animi, id est laborum et dolorum fug t harum quidem rerum facilis est et expedita voluptas assumenda est, omnis dolorr epellend poribus autem quibusdam et aut officiis.</p>
  <div class="abs read-more">READ MORE &gt;&gt;</div>
  <div class="abs media"><div class="media-fill" role="img" aria-label="Video still of a person working at a laptop showing a market chart on a bright desk"></div></div>
  <svg class="abs play" viewBox="0 0 60 60"><path d="M24 18l20 12-20 12z" fill="#fff"/></svg>
</section>

<section>
  <div class="abs services"></div>
  <h2 class="abs section-title" style="top:1106px">Services We Provide</h2>

  <svg class="abs" style="left:89px;top:1178px" width="56" height="46" viewBox="0 0 56 46"><ellipse cx="22" cy="18" rx="19" ry="14" stroke="#222" stroke-width="5" fill="none"/><path d="M10 30l-4 10 12-6" fill="#222"/><path d="M40 14c8 2 13 8 13 14 0 4-2 7-5 9l3 8-10-5" stroke="#222" stroke-width="4" fill="none"/></svg>
  <div class="abs" style="left:167px;top:1188px"><div class="svc-title">Management Consulting</div><p class="svc-copy">At vero eos et accusamus et iust odio dignissimos ducimus qui blanditiis pr aesentium voluptat.</p></div>

  <svg class="abs" style="left:465px;top:1176px" width="46" height="52" viewBox="0 0 46 52"><circle cx="23" cy="14" r="12" fill="#222"/><path d="M2 52c0-16 8-24 21-24s21 8 21 24z" fill="#222"/></svg>
  <div class="abs" style="left:534px;top:1188px"><div class="svc-title">Human Resources</div><p class="svc-copy">At vero eos et accusamus et iust odio dignissimos ducimus qui blanditiis pr aesentium voluptat.</p></div>

  <svg class="abs" style="left:815px;top:1178px" width="52" height="48" viewBox="0 0 52 48"><path d="M6 30V24a20 20 0 0 1 40 0v6" stroke="#222" stroke-width="5" fill="none"/><rect x="3" y="28" width="12" height="18" rx="3" fill="#222"/><rect x="37" y="28" width="12" height="18" rx="3" fill="#222"/></svg>
  <div class="abs" style="left:893px;top:1188px"><div class="svc-title">IT Services</div><p class="svc-copy">At vero eos et accusamus et iust odio dignissimos ducimus qui blanditiis pr aesentium voluptat.</p></div>

  <svg class="abs" style="left:89px;top:1316px" width="60" height="48" viewBox="0 0 60 48"><path d="M3 2v43h56" stroke="#222" stroke-width="4" fill="none"/><rect x="12" y="26" width="8" height="16" fill="#222"/><rect x="24" y="16" width="8" height="26" fill="#222"/><rect x="36" y="22" width="8" height="20" fill="#222"/><rect x="48" y="8" width="8" height="34" fill="#222"/></svg>
  <div class="abs" style="left:167px;top:1325px"><div class="svc-title">Customer Strategy</div><p class="svc-copy">At vero eos et accusamus et iust odio dignissimos ducimus qui blanditiis pr aesentium voluptat.</p></div>

  <svg class="abs" style="left:455px;top:1318px" width="60" height="40" viewBox="0 0 60 40"><rect x="2" y="2" width="56" height="36" fill="#222"/><rect x="8" y="8" width="44" height="24" fill="none" stroke="#f7d800" stroke-width="2"/><circle cx="30" cy="20" r="9" fill="#f7d800"/><rect x="28" y="14" width="4" height="12" fill="#222"/></svg>
  <div class="abs" style="left:534px;top:1325px"><div class="svc-title">Financial Services</div><p class="svc-copy">At vero eos et accusamus et iust odio dignissimos ducimus qui blanditiis pr aesentium voluptat.</p></div>

  <svg class="abs" style="left:815px;top:1314px" width="58" height="50" viewBox="0 0 58 50"><g fill="#222"><circle cx="20" cy="30" r="13"/><rect x="17" y="11" width="6" height="38"/><rect x="1" y="27" width="38" height="6"/><rect x="17" y="11" width="6" height="38" transform="rotate(45 20 30)"/><rect x="17" y="11" width="6" height="38" transform="rotate(-45 20 30)"/><circle cx="44" cy="14" r="9"/><rect x="42" y="1" width="4" height="26"/><rect x="31" y="12" width="26" height="4"/></g><circle cx="20" cy="30" r="5" fill="#f7d800"/><circle cx="44" cy="14" r="3.5" fill="#f7d800"/></svg>
  <div class="abs" style="left:893px;top:1325px"><div class="svc-title">Engineering</div><p class="svc-copy">At vero eos et accusamus et iust odio dignissimos ducimus qui blanditiis pr aesentium voluptat.</p></div>
</section>

<section>
  <h2 class="abs section-title" style="top:1520px">Recent Post</h2>

  <div class="abs card-img" style="left:97px;top:1592px;width:321px;height:210px"><div class="card-fill" role="img" aria-label="Hands using a calculator and pen over paperwork" style="background:linear-gradient(135deg,#f2f2f2,#c8c8c8 55%,#e6e6e6)"></div></div>
  <div class="abs date" style="left:90px;top:1732px">01<small>NOV</small></div>
  <div class="abs" style="left:97px;top:1817px"><div class="post-title">Finibus Bonorum et Malorum</div><p class="post-copy" style="margin-top:12px">Nam libero tempore, cum soluta nobis est eligendi optio cumque nihil impedit quo minus id quod maxim.</p><div class="post-rule" style="margin-top:14px"></div><div class="meta" style="margin-top:12px"><span>&#9632; Sam Rivers</span><span>&#9633; 3 Comments</span></div></div>

  <div class="abs card-img" style="left:440px;top:1592px;width:322px;height:210px"><div class="card-fill" role="img" aria-label="Video still of a team meeting around a table with printed charts" style="background:linear-gradient(180deg,#5c6f8e,#8fa5c4 55%,#dfe8f3)"></div></div>
  <svg class="abs play" style="left:578px;top:1770px;width:44px;height:44px" viewBox="0 0 60 60"><path d="M24 18l20 12-20 12z" fill="#fff"/></svg>
  <div class="abs date" style="left:433px;top:1732px">01<small>NOV</small></div>
  <div class="abs" style="left:440px;top:1817px"><div class="post-title">Finibus Bonorum et Malorum</div><p class="post-copy" style="margin-top:12px">Nam libero tempore, cum soluta nobis est eligendi optio cumque nihil impedit quo minus id quod maxim.</p><div class="post-rule" style="margin-top:14px"></div><div class="meta" style="margin-top:12px"><span>&#9632; Sam Rivers</span><span>&#9633; 3 Comments</span></div></div>

  <div class="abs card-img" style="left:784px;top:1592px;width:324px;height:210px"><div class="card-fill" role="img" aria-label="A businesswoman at a desk with documents and charts" style="background:linear-gradient(135deg,#b58f6a,#3a3a3a 45%,#e4e8ec)"></div></div>
  <div class="abs date" style="left:777px;top:1732px">01<small>NOV</small></div>
  <div class="abs" style="left:784px;top:1817px"><div class="post-title">Finibus Bonorum et Malorum</div><p class="post-copy" style="margin-top:12px">Nam libero tempore, cum soluta nobis est eligendi optio cumque nihil impedit quo minus id quod maxim.</p><div class="post-rule" style="margin-top:14px"></div><div class="meta" style="margin-top:12px"><span>&#9632; Sam Rivers</span><span>&#9633; 3 Comments</span></div></div>
</section>

<section>
  <div class="abs blog"></div>
  <h2 class="abs section-title" style="top:2036px">Our Blog</h2>
  <div class="abs blog-thumb" style="left:97px;top:2107px" role="img" aria-label="Colleagues reviewing work together"><div style="width:100%;height:100%;background:linear-gradient(135deg,#dfe7ef,#8aa3bd)"></div></div>
  <div class="abs" style="left:205px;top:2102px"><div class="blog-title">Finibus Bono Malorum</div><div class="blog-date">&#9638; 10/12/2016</div></div>
  <div class="abs blog-thumb" style="left:457px;top:2107px" role="img" aria-label="A businessman standing in an office"><div style="width:100%;height:100%;background:linear-gradient(135deg,#c9a27a,#2f3440)"></div></div>
  <div class="abs" style="left:565px;top:2102px"><div class="blog-title">Finibus Bono Malorum</div><div class="blog-date">&#9638; 10/12/2016</div></div>
  <div class="abs blog-thumb" style="left:816px;top:2107px" role="img" aria-label="Hands signing a document"><div style="width:100%;height:100%;background:linear-gradient(135deg,#eef0f2,#9db2c6)"></div></div>
  <div class="abs" style="left:924px;top:2102px"><div class="blog-title">Finibus Bono Malorum</div><div class="blog-date">&#9638; 10/12/2016</div></div>
  <div class="abs accent-rule"></div>
</section>

<footer>
  <div class="abs" style="left:99px;top:2272px"><div class="foot-title">Information</div>
    <ul class="foot-list"><li>Home</li><li>About us</li><li>Services</li><li>Blog</li><li>Insights &amp; News</li><li>Resources</li><li>Contact Us</li></ul></div>
  <div class="abs" style="left:288px;top:2272px"><div class="foot-title">Resources</div>
    <ul class="foot-list"><li>Our Story</li><li>Team</li><li>Newsletters</li><li>Contact</li><li>Jobs</li><li>Help Us Grow</li></ul></div>
  <div class="abs" style="left:518px;top:2272px"><div class="foot-title">Newsletter Subscription</div>
    <p class="body-copy" style="margin-top:14px;width:230px;font-size:12px">Register your Email Address to get Information about us</p></div>
  <div class="abs input">Email Address</div>
  <div class="abs subscribe">SUBSCRIBE</div>
  <div class="abs" style="left:864px;top:2272px"><div class="foot-title">KV contact information</div>
    <div class="contact-row" style="margin-top:14px"><svg width="10" height="14" viewBox="0 0 10 14"><path d="M5 0a5 5 0 0 1 5 5c0 4-5 9-5 9S0 9 0 5a5 5 0 0 1 5-5z" fill="#666"/><circle cx="5" cy="5" r="2" fill="#fff"/></svg><span>Orchard Lane 42, Suite 7, <br>30310 Marlow City</span></div>
    <div class="contact-row" style="margin-top:18px"><svg width="12" height="12" viewBox="0 0 24 24"><path fill="#666" d="M6.6 10.8a15 15 0 0 0 6.6 6.6l2.2-2.2c.3-.3.7-.4 1-.2 1.1.4 2.3.6 3.6.6.6 0 1 .4 1 1V20c0 .6-.4 1-1 1A17 17 0 0 1 3 4c0-.6.4-1 1-1h3.5c.6 0 1 .4 1 1 0 1.3.2 2.5.6 3.6.1.3 0 .7-.2 1z"/></svg><span>555-210-4471</span></div>
    <div class="contact-row" style="margin-top:18px"><svg width="13" height="10" viewBox="0 0 24 18"><rect x="1" y="1" width="22" height="16" fill="#666"/><path d="M1 1l11 9 11-9" stroke="#fff" stroke-width="2" fill="none"/></svg><span>hello@kindredvantage.org</span></div>
  </div>
  <div class="abs bottom-rule"></div>
  <div class="abs copyright">Copyrights © 2016, Kindred Vantage. All rights reserved.</div>
  <div class="abs" style="left:976px;top:2507px;display:flex;gap:10px">
    <span class="social"></span><span class="social"></span><span class="social"></span><span class="social"></span>
  </div>
</footer>

</body>
</html>
```